Music Festival in Colorado Needs Awesome Flier Design

We need an eye-catching & captivating flier design for an annual music festival in Denver, CO (USA). The festival features the best Colorado musicians within the genres of jam - funk - bluegrass - electronic - reggae - rock.

The design should look clean and professional while still being creative and unique. The past three years' flier designs are attached, as well as the logo and some other designs that match the aesthetic of what we're looking for.

This festival has a big element of Colorado pride so any

Target Market(s)

Hippies - live music enthusiasts - partiers. Ages 21 - 40.

Industry/Entity Type

Entertainment

Colors
0355a3
ec1f27
ffffff
fbed22

Requirements
Must have
• Attached design text.
Nice to have
• - Quality texture and psychedelic elements.
• - Colorado pride elements; color scheme (red, white, blue & yellow), flag, ect.
• - Nature elements are awesome but this is also a downtown festival so keep that in mind.
Should not have
• Cheesy artwork.

```html
<!DOCTYPE html>
<html lang="en">
<head>
<meta charset="utf-8">
<title>Carry the Sound – Colorado Music Festival 2018</title>
<link rel="stylesheet" href="https://fonts.googleapis.com/css2?family=Fira+Sans:wght@800&family=Fira+Sans+Condensed:wght@600;700;800&family=Kaushan+Script&family=Oswald:wght@300&display=swap">
<style>
  :root{
    --sky:#f8d45a;
    --sky-light:#fbe48a;
    --ridge:#6a5fa8;
    --hill:#4f9a45;
    --forest:#2f7340;
    --forest-deep:#1d5a37;
    --ink:#1c1a17;
    --plum:#3b2d6f;
    --white:#ffffff;
    --gold:#f6d84a;
  }
  *{margin:0;padding:0;box-sizing:border-box}
  html,body{width:848px;height:1200px;overflow:hidden;background:var(--white)}
  .flier{position:relative;width:848px;height:1200px;overflow:hidden}
  .landscape{
    position:absolute;inset:0;
    background:linear-gradient(180deg,
      var(--sky-light) 0%,
      var(--sky) 34%,
      #e9b86a 40%,
      var(--ridge) 47%,
      #5b73a8 55%,
      var(--hill) 62%,
      var(--forest) 78%,
      var(--forest-deep) 100%);
  }
  .edition{
    position:absolute;top:40px;left:0;width:100%;text-align:center;
    font-family:"Kaushan Script",cursive;font-size:72px;color:var(--plum);
  }
  .edition sup{font-size:40px;vertical-align:32px}
  .festival-name{
    position:absolute;top:178px;left:0;width:100%;text-align:center;
    font-family:"Fira Sans Condensed",sans-serif;font-weight:800;color:var(--ink);
    text-transform:uppercase;line-height:.9;
  }
  .festival-name .lead{display:block;font-size:44px;letter-spacing:1px}
  .festival-name .main{display:block;font-size:150px;letter-spacing:-2px}
  .tagline{
    position:absolute;top:398px;left:0;width:100%;text-align:center;
    font-family:"Oswald",sans-serif;font-weight:300;font-size:20px;letter-spacing:4px;
    color:var(--ink);text-transform:uppercase;
  }
  .dates{
    position:absolute;top:442px;left:190px;width:468px;height:78px;
    background:var(--plum);color:var(--white);
    font-family:"Fira Sans Condensed",sans-serif;font-weight:800;font-size:42px;
    display:flex;align-items:center;justify-content:center;text-transform:uppercase;
  }
  .lineup{
    position:absolute;top:720px;left:62px;width:730px;
    color:var(--white);font-family:"Fira Sans Condensed",sans-serif;font-weight:700;
    text-shadow:0 2px 6px rgba(0,0,0,.35);
  }
  .headliner{font-family:"Fira Sans",sans-serif;font-weight:800;font-size:88px;letter-spacing:-2px;line-height:1.05;white-space:nowrap}
  .tier-two{font-size:46px;line-height:1.15;white-space:nowrap}
  .tier-three{font-size:34px;line-height:1.32;white-space:nowrap}
  .venue{
    position:absolute;top:1070px;left:62px;
    font-family:"Fira Sans Condensed",sans-serif;font-weight:600;font-size:21px;line-height:1.32;
    color:var(--gold);font-style:normal;
  }
  .tickets{position:absolute;top:1070px;left:320px;width:480px}
  .tickets-label{
    font-family:"Oswald",sans-serif;font-weight:300;font-size:32px;letter-spacing:9px;
    color:var(--white);text-transform:uppercase;
  }
  .tickets-url{
    font-family:"Fira Sans",sans-serif;font-weight:800;font-size:33px;color:var(--gold);
    letter-spacing:-.5px;margin-top:2px;
  }
</style>
</head>
<body>
<main class="flier">
  <div class="landscape" role="img" aria-label="Illustrated Colorado landscape: pine-covered green hills and purple mountain ridges under a yellow sky with clouds and a setting sun, overlaid with a woven texture"></div>

  <p class="edition">6<sup>th</sup> Annual</p>

  <h1 class="festival-name">
    <span class="lead">Carry the</span>
    <span class="main">Sound</span>
  </h1>
  <p class="tagline">Colorado Music Festival</p>

  <p class="dates">May 11th - 13th, 2018</p>

  <section class="lineup">
    <p class="headliner">Reed Calloway Band</p>
    <p class="tier-two">• Allhands Orchestra • Split Theory</p>
    <p class="tier-three">• The Lucky Sprouts • B-Ray &amp; The Summit • Wapiti</p>
    <p class="tier-three">• Helixes • Foothill Ensemble • Sunsoaked • Paratonics</p>
    <p class="tier-three">• Prismatic • Clear Horizon • Rail Junction • Orbits</p>
  </section>

  <address class="venue">
    Larkspur Yard<br>
    418 W. 27th Ave<br>
    Denver, CO 80205
  </address>

  <div class="tickets">
    <p class="tickets-label">Tickets &amp; More Info @</p>
    <p class="tickets-url">www.carrythesoundfest.com</p>
  </div>
</main>
</body>
</html>
```